New Brochure for existing Virtual Reality Amusement Arena

I need a two sided half page brochure for my arcade. it needs to say what we do and what we have to offer. It basically needs to be a paper copy of all the information thats on my website www.kavimo-nix.com
Please check that as it is very informative!
Industry/Entity Type
Entertainment
Colors
Designer to choose colors to be used in the design.
Requirements
Must have
- Color. I have uploaded an old brochure I had made, but now we have a new company and new logo, please make it similar to that. Please pull all pics from my website www.kavimo-nix.com
Should not have
- useless information

```html
<!DOCTYPE html>
<html lang="en">
<head>
<meta charset="utf-8">
<title>Kavimo-Nix VR Arena Brochure</title>
<link rel="stylesheet" href="https://fonts.googleapis.com/css2?family=Roboto+Condensed:wght@700&family=Source+Sans+3:wght@400;600;700&display=swap">
<style>
  :root {
    --page: #ffffff;
    --ink-dark: #1e1e1f;
    --ink-mid: #3a3a3c;
    --grey-light: #8d8d8f;
    --red: #c8141e;
    --red-deep: #7d0f16;
    --red-wine: #5a1a20;
    --white: #ffffff;
    --text-dark: #1a1a1a;
  }
  * { margin: 0; padding: 0; box-sizing: border-box; }
  html, body { width: 1200px; height: 900px; overflow: hidden; background: var(--page); }
  .canvas { position: relative; width: 1200px; height: 900px; }

  .brochure {
    position: absolute; left: 118px; top: 97px; width: 965px; height: 681px;
    overflow: hidden; background: var(--ink-dark);
  }
  .panel { position: absolute; top: 0; height: 681px; overflow: hidden; }
  .panel--left { left: 0; width: 482px; background: linear-gradient(160deg, var(--ink-dark) 0%, var(--ink-mid) 45%, var(--grey-light) 100%); }
  .panel--right { left: 482px; width: 483px; background: linear-gradient(150deg, var(--red-wine) 0%, #6e3a3e 45%, #9a8a8b 100%); }
  .stripes { position: absolute; inset: 0; width: 100%; height: 100%; }

  .headline {
    position: absolute; left: 46px; top: 74px; color: var(--white);
    font-family: "Roboto Condensed", "Arial Narrow", sans-serif; font-weight: 700;
    line-height: 1; letter-spacing: 0.5px;
  }
  .headline__top { display: block; font-size: 42px; }
  .headline__main { display: block; font-size: 60px; margin-top: 4px; }

  .intro, .entry-note {
    font-family: "Source Sans 3", "Myriad Pro", sans-serif; font-weight: 600;
    color: var(--white); font-size: 13.5px; line-height: 17px;
  }
  .intro { position: absolute; left: 46px; top: 192px; width: 420px; }

  .entry-note { position: absolute; left: 42px; top: 270px; width: 392px; height: 66px; padding: 4px 16px 0 32px; }
  .entry-note__bracket { position: absolute; top: 0; width: 14px; height: 66px; border: 3px solid var(--white); }
  .entry-note__bracket--open { left: 0; border-right: none; }
  .entry-note__bracket--close { right: 0; border-left: none; }

  .photo { position: absolute; }
  .photo--player-left {
    left: 312px; top: 358px; width: 140px; height: 323px;
    background: linear-gradient(180deg, #4a4a4c 0%, #8b8b8d 45%, #6a6a6c 100%);
    border-radius: 60px 60px 0 0;
  }
  .photo--player-right {
    left: 250px; top: 40px; width: 233px; height: 558px;
    background: radial-gradient(ellipse at 50% 40%, #a59596 0%, #7b5a5d 55%, rgba(90,26,32,0) 100%);
  }

  .contact-band {
    position: absolute; left: 0; top: 596px; width: 482px; height: 85px;
    background: linear-gradient(90deg, var(--red-deep) 0%, #a3121b 100%);
    border-top: 5px solid var(--white);
  }
  .contact-band__phone {
    position: absolute; left: 42px; top: 21px; color: var(--white);
    font-family: "Source Sans 3", "Myriad Pro", sans-serif; font-weight: 600; font-size: 18px;
  }
  .contact-band__address {
    position: absolute; left: 42px; top: 47px; color: var(--white);
    font-family: "Source Sans 3", "Myriad Pro", sans-serif; font-weight: 600; font-size: 13.5px;
  }

  .brand {
    position: absolute; left: 62px; top: 38px; display: flex; align-items: center; gap: 10px;
    color: var(--white); font-family: "Roboto Condensed", "Arial Narrow", sans-serif;
    font-weight: 700; font-size: 31px; letter-spacing: 2px;
  }
  .brand__mark { width: 30px; height: 30px; border-radius: 50%; background: var(--white); }

  .tagline {
    position: absolute; left: 25px; top: 205px; color: var(--white);
    font-family: "Roboto Condensed", "Arial Narrow", sans-serif; font-weight: 700;
    font-size: 58px; line-height: 56px; letter-spacing: 0.5px;
  }

  .feature-band {
    position: absolute; left: 0; top: 598px; width: 483px; height: 83px;
    background: linear-gradient(90deg, #dcdcdc 0%, var(--white) 40%);
    clip-path: polygon(20px 0, 100% 0, 100% 100%, 50px 100%);
  }
  .feature-band__text {
    position: absolute; left: 84px; top: 26px; color: var(--text-dark);
    font-family: "Source Sans 3", "Myriad Pro", sans-serif; font-weight: 700; font-size: 14.5px; letter-spacing: 0.3px;
  }
  .web-tab {
    position: absolute; right: 0; bottom: 0; width: 194px; height: 21px; background: var(--ink-dark);
    clip-path: polygon(8px 0, 100% 0, 100% 100%, 0 100%);
    color: var(--white); font-family: "Source Sans 3", "Myriad Pro", sans-serif; font-weight: 600;
    font-size: 10.5px; letter-spacing: 1.5px; line-height: 21px; padding-left: 34px;
  }
</style>
</head>
<body>
<div class="canvas">
  <div class="brochure">

    <section class="panel panel--left">
      <svg class="stripes" viewBox="0 0 482 681" preserveAspectRatio="none" aria-hidden="true">
        <polygon points="0,150 0,600 150,600 " fill="#c8141e" opacity="0.9"/>
        <polygon points="0,60 40,60 330,600 190,600 0,260" fill="#d4171f" opacity="0.85"/>
        <polygon points="90,0 200,0 482,500 482,600 420,600" fill="#ffffff" opacity="0.08"/>
        <polygon points="250,0 330,0 482,270 482,420" fill="#ffffff" opacity="0.12"/>
      </svg>
      <h1 class="headline">
        <span class="headline__top">GAMING LIKE YOU’VE</span>
        <span class="headline__main">NEVER SEEN</span>
      </h1>
      <p class="intro">Home of Tampa's one of a kind video game experience. Fully immersive VR, state of the art tech. A completely new play experience for everyone!</p>
      <div class="entry-note">
        <span class="entry-note__bracket entry-note__bracket--open"></span>
        Just walk right in. Up to eight people can enter at once at stay to try all our products. A new group comes in every 2 hours. Group and entrance times are as follows
        <span class="entry-note__bracket entry-note__bracket--close"></span>
      </div>
      <div class="contact-band">
        <p class="contact-band__phone">CALL US TODAY-813.555.0142</p>
        <p class="contact-band__address">2190 W Larkspur Ave, Tampa FL 33607</p>
      </div>
      <div class="photo photo--player-left" role="img" aria-label="Photo of a player standing in a VR headset holding motion controllers"></div>
    </section>

    <section class="panel panel--right">
      <svg class="stripes" viewBox="0 0 483 681" preserveAspectRatio="none" aria-hidden="true">
        <polygon points="0,120 0,330 150,598 270,598" fill="#c8141e" opacity="0.85"/>
        <polygon points="120,0 220,0 483,450 483,598 420,598" fill="#b0121b" opacity="0.75"/>
        <polygon points="300,0 380,0 483,180 483,320" fill="#ffffff" opacity="0.1"/>
      </svg>
      <div class="photo photo--player-right" role="img" aria-label="Photo of a player wearing a VR headset and backpack computer holding a controller"></div>
      <div class="brand"><span class="brand__mark"></span>KAVIMO-NIX</div>
      <p class="tagline">BECAUSE<br>THAT’S<br>WHERE<br>ALL THE<br>FUN IS</p>
      <div class="feature-band">
        <p class="feature-band__text">FULLY IMMERSIVE WITH WALKING ABILITY</p>
      </div>
      <div class="web-tab">www.kavimo-nix.com</div>
    </section>

  </div>
</div>
</body>
</html>
```